Business Card Design - Tobden Group.

Tobden Group is a small independent technology and business consulting business. The name is derived from the first 3 letters of my son Gregory and Daughter Ruth's names. I am looking for something that is a simple yet elegant somewhat traditional or formal design. I would like to see the logo accentuate the W and M in the design. This is a business that is what I would describe as my personal business and is separate from my full time day job.Most of our consulting projects are specialized and focus in the solid state lighting, compound semiconductor and material sciences markets and subjects. We are in a highly specialized niche. Which is why a simple design for the logo and theme which can utilized into business stationary might be the best way to go.

Industry/Entity Type

Business

Contact Information for Business Card

Tobden Group, LLCBruce S RylancePrincipal, CEO818 Larchmont LaneLake Forest, IL 60318

Font styles to use
Serif
Sans Serif

Colors
0355a3
00a990
34a7d8

Requirements
Must have
• Simple but elegant design
Nice to have
• I have selected colors i like but am open to what designers would like to suggest.
Should not have
• a lot of pictures or icons

```html
<!DOCTYPE html>
<html lang="en">
<head>
<meta charset="utf-8">
<title>Tobden Group, LLC – Business Card</title>
<link href="https://fonts.googleapis.com/css2?family=Oswald:wght@400;500&display=swap" rel="stylesheet">
<style>
  :root {
    --brand-blue: #0356a5;
    --ink: #262626;
    --paper: #ffffff;
  }
  * { margin: 0; padding: 0; box-sizing: border-box; }
  html, body { width: 1200px; height: 702px; overflow: hidden; background: var(--paper); }
  .card {
    position: relative;
    width: 1200px;
    height: 702px;
    background: var(--paper);
    font-family: "Oswald", "Arial Narrow", sans-serif;
    color: var(--ink);
  }
  .brand {
    position: absolute;
    left: 40px;
    width: 420px;
    top: 296px;
    text-align: center;
    color: var(--brand-blue);
    font-weight: 500;
    font-size: 42px;
    letter-spacing: 2px;
    text-transform: uppercase;
    line-height: 1;
  }
  .divider {
    position: absolute;
    left: 497px;
    top: 174px;
    width: 3px;
    height: 355px;
    background: var(--brand-blue);
  }
  .person {
    position: absolute;
    left: 535px;
    top: 206px;
  }
  .person-name {
    font-weight: 500;
    font-size: 62px;
    line-height: 1;
    letter-spacing: 1px;
    color: var(--ink);
  }
  .person-title {
    margin-top: 14px;
    font-weight: 500;
    font-size: 38px;
    line-height: 1;
    letter-spacing: 2px;
    color: var(--brand-blue);
  }
  .contact-list {
    list-style: none;
    margin-top: 16px;
  }
  .contact-item {
    display: flex;
    align-items: center;
    height: 55px;
    font-size: 35px;
    letter-spacing: 1px;
    color: var(--ink);
  }
  .contact-icon {
    width: 30px;
    height: 30px;
    margin-right: 24px;
    flex: none;
    fill: var(--brand-blue);
  }
  .footer-bands {
    position: absolute;
    left: 0;
    bottom: 0;
    width: 1200px;
    height: 40px;
  }
  .band { position: absolute; top: 0; height: 40px; }
  .band-left { left: 0; width: 348px; background: var(--brand-blue); }
  .band-center { left: 357px; width: 486px; background: var(--ink); }
  .band-right { left: 852px; width: 348px; background: var(--brand-blue); }
</style>
</head>
<body>
  <div class="card">
    <div class="brand">Tobden Group, LLC</div>

    <div class="divider"></div>

    <div class="person">
      <div class="person-name">Dennis K Harrow</div>
      <div class="person-title">Principal, CEO</div>

      <ul class="contact-list">
        <li class="contact-item">
          <svg class="contact-icon" viewBox="0 0 24 24" aria-hidden="true">
            <path d="M12 1C7.6 1 4.5 4.2 4.5 8.4 4.5 14 12 23 12 23s7.5-9 7.5-14.6C19.5 4.2 16.4 1 12 1zm0 10.6a3.1 3.1 0 1 1 0-6.2 3.1 3.1 0 0 1 0 6.2z"/>
          </svg>
          <span>426 Pebbleford Lane Elm Ridge, IL 60318</span>
        </li>
        <li class="contact-item">
          <svg class="contact-icon" viewBox="0 0 24 24" aria-hidden="true">
            <path d="M1 9c0-3 5-5 11-5s11 2 11 5v2h-5V8.5c-1.8-.6-3.8-.9-6-.9s-4.2.3-6 .9V11H1V9z"/>
            <path d="M7 10h10l4 6v5H3v-5l4-6zm5 2.5a3 3 0 1 0 0 6 3 3 0 0 0 0-6z"/>
          </svg>
          <span>847-555-0142</span>
        </li>
        <li class="contact-item">
          <svg class="contact-icon" viewBox="0 0 24 24" aria-hidden="true">
            <path d="M1 5h22v1.2L12 13 1 6.2V5z"/>
            <path d="M1 8.4l11 6.8 11-6.8V19H1V8.4z"/>
          </svg>
          <span>dharrow@tobden-grp.com</span>
        </li>
      </ul>
    </div>

    <div class="footer-bands">
      <div class="band band-left"></div>
      <div class="band band-center"></div>
      <div class="band band-right"></div>
    </div>
  </div>
</body>
</html>
```